Business Card Design for Software Development Company

I am looking for a business card design the incorporates my new logo (attached below).

Key information to include:
Name: Darnell Whisket
Title: CEO
Email: darnell@brovatecore.com
Phone: 418-926-7301
Website: www.brovatecore.com

NOTE: This design should be easy to edit so that we can order cards for different members of our team.

```html
<!DOCTYPE html>
<html lang="en">
<head>
<meta charset="utf-8">
<title>BrovateCore Business Card</title>
<link rel="stylesheet" href="https://fonts.googleapis.com/css2?family=Montserrat:wght@500;700&family=Lato:wght@400&display=swap">
<style>
  :root {
    --stage: #2b2b2d;
    --orange: #e2761f;
    --orange-deep: #d46a1c;
    --paper: #f7f7f7;
    --navy: #243047;
    --ink: #3a3f48;
    --white: #ffffff;
  }
  * { box-sizing: border-box; margin: 0; padding: 0; }
  html, body { width: 1200px; height: 900px; overflow: hidden; }
  body {
    background: var(--stage);
    display: flex;
    flex-direction: column;
    align-items: center;
    justify-content: center;
    gap: 60px;
  }
  .card {
    width: 600px;
    height: 343px;
    border-radius: 34px;
    position: relative;
    overflow: hidden;
  }
  .card-back {
    background: linear-gradient(135deg, var(--orange-deep), var(--orange));
    display: flex;
    align-items: center;
    justify-content: center;
  }
  .brand { display: flex; flex-direction: column; align-items: flex-end; }
  .brand-name {
    font-family: "Montserrat", sans-serif;
    font-weight: 700;
    font-size: 50px;
    letter-spacing: -1px;
    line-height: 1;
  }
  .brand-tag {
    font-family: "Montserrat", sans-serif;
    font-weight: 700;
    font-size: 7px;
    letter-spacing: 0.4px;
    margin-top: 4px;
  }
  .card-back .brand-name, .card-back .brand-tag { color: var(--white); }
  .card-front { background: linear-gradient(120deg, #e9e9e9 0%, var(--paper) 45%, var(--white) 100%); }
  .card-front .brand {
    position: absolute;
    left: 46px;
    top: 70px;
    flex-direction: row;
    align-items: center;
    gap: 12px;
  }
  .brand-mark { width: 26px; height: 26px; border-radius: 50%; background: var(--orange); }
  .brand-text { display: flex; flex-direction: column; align-items: flex-end; }
  .card-front .brand-name, .card-front .brand-tag { color: var(--navy); }
  .details {
    position: absolute;
    right: 40px;
    bottom: 58px;
    display: flex;
    align-items: stretch;
    gap: 18px;
  }
  .person { display: flex; flex-direction: column; align-items: flex-end; justify-content: flex-end; }
  .person-title {
    font-family: "Lato", sans-serif;
    font-size: 15px;
    color: var(--ink);
    letter-spacing: 1px;
  }
  .person-name {
    font-family: "Montserrat", sans-serif;
    font-weight: 700;
    font-size: 16px;
    color: var(--orange);
    letter-spacing: 1px;
    text-transform: uppercase;
  }
  .divider { width: 1px; background: var(--navy); }
  .contact-list { list-style: none; display: flex; flex-direction: column; gap: 6px; }
  .contact-item {
    display: flex; align-items: center; gap: 9px;
    font-family: "Lato", sans-serif;
    font-size: 14px;
    color: var(--ink);
  }
  .contact-icon { width: 15px; height: 15px; flex: none; }
</style>
</head>
<body>
  <section class="card card-back">
    <div class="brand">
      <span class="brand-name">BrovateCore</span>
      <span class="brand-tag">A DIVISION OF BROVATE GROUP</span>
    </div>
  </section>

  <section class="card card-front">
    <div class="brand">
      <span class="brand-mark"></span>
      <div class="brand-text">
        <span class="brand-name">BrovateCore</span>
        <span class="brand-tag">A DIVISION OF BROVATE GROUP</span>
      </div>
    </div>

    <div class="details">
      <div class="person">
        <span class="person-title">CEO</span>
        <span class="person-name">Darnell Whisket</span>
      </div>
      <span class="divider"></span>
      <ul class="contact-list">
        <li class="contact-item">
          <svg class="contact-icon" viewBox="0 0 24 24"><path fill="#e2761f" d="M6.6 10.8a15 15 0 0 0 6.6 6.6l2.2-2.2c.3-.3.7-.4 1-.2 1.1.4 2.3.6 3.6.6.6 0 1 .4 1 1V20c0 .6-.4 1-1 1A17 17 0 0 1 3 4c0-.6.4-1 1-1h3.5c.6 0 1 .4 1 1 0 1.3.2 2.5.6 3.6.1.3 0 .7-.2 1z"/></svg>
          <span>418-926-7301</span>
        </li>
        <li class="contact-item">
          <svg class="contact-icon" viewBox="0 0 24 24"><rect x="2" y="5" width="20" height="14" rx="1" fill="#e2761f"/><path d="M2 6l10 7 10-7" fill="none" stroke="#fff" stroke-width="1.6"/></svg>
          <span>darnell@brovatecore.com</span>
        </li>
        <li class="contact-item">
          <svg class="contact-icon" viewBox="0 0 24 24" fill="none" stroke="#e2761f" stroke-width="1.6"><circle cx="12" cy="12" r="10"/><ellipse cx="12" cy="12" rx="4.5" ry="10"/><path d="M2 12h20M4 7h16M4 17h16"/></svg>
          <span>www.brovatecore.com</span>
        </li>
      </ul>
    </div>
  </section>
</body>
</html>
```